A very simple 3-4 page website, wine consluting
A comprehensive and clear design brief is included
Beverages
www.veLumaconsulting.example
see brief
left side
JPG company logo, many formats available
EPS company logo, many formats available
Website Brief
my photo, not required
For Gavin
for Gavin

```html
<!DOCTYPE html>
<html lang="en">
<head>
<meta charset="utf-8">
<title>veLuma consulting – Services</title>
<link rel="stylesheet" href="https://fonts.googleapis.com/css2?family=Arimo:ital,wght@0,400;0,700;1,400&display=swap">
<style>
  :root {
    --red: #d01820;
    --red-dark: #8e0d12;
    --red-light: #e8343a;
    --ink: #222222;
    --brand-ink: #3a3a3a;
    --muted: #8a8a8a;
    --grey-top: #b9b9b9;
    --grey-bottom: #ffffff;
    --panel: #ffffff;
    --rule: #d6d6d6;
  }
  * { margin: 0; padding: 0; box-sizing: border-box; }
  html, body { width: 1200px; height: 1000px; overflow: hidden; }
  body {
    position: relative;
    font-family: "Arimo", Arial, sans-serif;
    color: var(--ink);
    background: linear-gradient(to bottom, var(--grey-top) 0, #e4e4e4 260px, var(--grey-bottom) 520px);
  }

  /* Brand */
  .brand {
    position: absolute; left: 300px; top: 42px; width: 560px;
    text-align: center;
  }
  .brand-name { font-size: 58px; font-weight: 400; color: var(--brand-ink); letter-spacing: 1px; line-height: 1; }
  .brand-tagline {
    position: absolute; left: 560px; top: 124px;
    font-size: 15px; color: #666; font-style: italic;
  }

  /* Navigation band */
  .nav-band {
    position: absolute; left: 890px; top: 150px; width: 170px; height: 420px;
    border-radius: 0 90px 90px 0;
    background: linear-gradient(to right, var(--red-dark), var(--red) 45%, var(--red-light));
    box-shadow: 4px 6px 14px rgba(0,0,0,.25);
  }
  .main-nav { position: absolute; left: 955px; top: 208px; list-style: none; }
  .main-nav li { margin-bottom: 12px; }
  .main-nav a {
    display: block; padding: 3px 10px; font-size: 17px; color: #fff; text-decoration: none;
  }
  .main-nav a.is-current { background: rgba(255,255,255,.25); border-radius: 3px; }

  /* Content panel */
  .content-panel {
    position: absolute; left: 157px; top: 197px; width: 733px; height: 663px;
    background: var(--panel); border-radius: 10px;
    box-shadow: 0 4px 18px rgba(0,0,0,.22);
  }
  .page-title { position: absolute; left: 58px; top: 40px; font-size: 40px; font-weight: 400; }
  .intro { position: absolute; left: 58px; top: 100px; width: 620px; font-size: 14px; line-height: 1.35; }
  .intro p + p { margin-top: 14px; }

  .service-circles { position: absolute; left: 48px; top: 232px; display: flex; }
  .service {
    width: 200px; height: 200px; border-radius: 50%;
    margin-right: 24px;
    background: radial-gradient(circle at 50% 35%, var(--red-light), var(--red) 55%, var(--red-dark));
    box-shadow: 0 4px 10px rgba(0,0,0,.3);
    color: #fff; text-align: center; padding: 30px 24px 0;
  }
  .service:last-child { margin-right: 0; }
  .service h2 { font-size: 18px; font-weight: 400; padding-bottom: 5px; border-bottom: 1px solid rgba(255,255,255,.7); margin-bottom: 8px; }
  .service h2.small { font-size: 12.5px; font-weight: 700; line-height: 1.15; }
  .service li { list-style: none; font-size: 11px; line-height: 1.2; padding: 2px 0; border-bottom: 1px solid rgba(255,255,255,.35); }
  .service li:last-child { border-bottom: 0; }
  .service p { font-size: 11px; line-height: 1.3; }

  .testimonial-rule { position: absolute; left: 58px; top: 500px; width: 620px; border-top: 1px solid var(--rule); }
  .testimonial-quote {
    position: absolute; left: 58px; top: 530px; width: 390px;
    font-size: 13px; font-style: italic; color: var(--muted); line-height: 1.5;
  }
  .testimonial-quote::before { content: "\201C"; font-size: 36px; color: #bbb; line-height: 0; vertical-align: -12px; margin-right: 4px; }
  .testimonial-side { position: absolute; left: 490px; top: 528px; width: 220px; }
  .testimonial-side h3 { font-size: 16px; font-weight: 400; color: #555; margin-bottom: 16px; }
  .testimonial-side .person { font-size: 13px; color: #555; }
  .testimonial-side .role { font-size: 10px; color: var(--muted); line-height: 1.35; margin-top: 4px; }

  /* Footer */
  .site-footer {
    position: absolute; left: 170px; top: 884px; width: 730px;
    display: flex; align-items: center; gap: 42px; font-size: 12px; color: #555;
  }
  .footer-brand { margin-left: auto; font-size: 22px; color: #888; }
</style>
</head>
<body>
  <header>
    <div class="brand">
      <span class="brand-name">veLuma consulting</span>
    </div>
    <div class="brand-tagline">the China wine market insider</div>
  </header>

  <div class="nav-band"></div>
  <ul class="main-nav">
    <li><a href="#">Home</a></li>
    <li><a href="#">About Us</a></li>
    <li><a href="#" class="is-current">Services</a></li>
    <li><a href="#">Contact</a></li>
  </ul>

  <main class="content-panel">
    <h1 class="page-title">Services</h1>
    <div class="intro">
      <p>In order to succeed in this challenging, opaque and unique market you need a market insider who can work with you to achieve your goals. veLuma consulting, with over nine years of experience, is your China wine market insider</p>
      <p>veLuma consulting can greatly increase your effectiveness by first exploring your needs and then develop effective solutions address all of your unique challenges.</p>
    </div>

    <section class="service-circles">
      <article class="service">
        <h2>Wine Producers</h2>
        <ul>
          <li>Product Development (packaging, naming, wine style)</li>
          <li>Market Entry</li>
          <li>In Market Promotion</li>
        </ul>
      </article>
      <article class="service">
        <h2 class="small">Trade Organizations &amp; Governmental Bodies</h2>
        <ul>
          <li>Wine Conference Presentations</li>
          <li>Standard Market Reports</li>
          <li>Customized Market Reports</li>
          <li>Effective In Market Promotion Strategies</li>
        </ul>
      </article>
      <article class="service">
        <h2>Journalists</h2>
        <p>Please contact us for expert opinions and analysis of the bottled wine market in Mainland China, and the evolving culture of wine in China.</p>
      </article>
    </section>

    <div class="testimonial-rule"></div>
    <blockquote class="testimonial-quote">I can highly recommend his [veLuma consulting] services to any other commercial bureau, advocacy group, promotional organisation, trade body, or winery.</blockquote>
    <aside class="testimonial-side">
      <h3>What others say about us</h3>
      <div class="person">Marco Delgado</div>
      <div class="role">Chief Economic and Commercial Counselor, Trade Office of Valmera (Beijing)</div>
    </aside>
  </main>

  <footer class="site-footer">
    <span>info@veLumaconsulting.example</span>
    <span>Skype: veluma.consulting</span>
    <span>Tel: +852 5550 0142</span>
    <span class="footer-brand">veLuma</span>
  </footer>
</body>
</html>
```